Design a beautiful book cover for my self help book

The Craft of Hush is a book I've written about how I learnt to quite my mind, rid myself of old pain and stand in my intuition. It's one simple practical tool to find you moment and step into your abundance. We need a cover that reflects this amazing concept! The current cover is attached. It's too dark and not in tune with the market. Please search books with similar content and make design similar yet different.

Target Market(s)

People into self help or motivational content. As well as people suffering from depression, stress, anxiety etc.

Industry/Entity Type

Self Help

Requirements
Must have
• A light airy feel of freedom
Nice to have
• Some sort of linage from current cover
Should not have
• Dark, ambiguous,

```html
<!DOCTYPE html>
<html lang="en">
<head>
<meta charset="utf-8">
<title>The Craft of Hush — Book Cover</title>
<link href="https://fonts.googleapis.com/css2?family=Baskervville&family=Mrs+Saint+Delafield&display=swap" rel="stylesheet">
<style>
  :root {
    --paper: #ffffff;
    --sky: #a9c1c9;
    --halo: #b3c9d0;
    --slate: #547183;
    --ink: #2b3f4a;
    --body-ink: #1c2a31;
    --line: #eef5f8;
    --label: #f0f6fa;
    --sprout-tone: #c3d5db;
  }
  html, body {
    margin: 0;
    padding: 0;
    width: 1200px;
    height: 933px;
    overflow: hidden;
    background: var(--paper);
  }
  .cover {
    position: relative;
    width: 1200px;
    height: 933px;
    font-family: "Baskervville", "Libre Baskerville", serif;
  }
  .cover-art {
    position: absolute;
    inset: 0;
    width: 1200px;
    height: 933px;
  }
  .blurb {
    position: absolute;
    left: 87px;
    top: 98px;
    width: 470px;
    margin: 0;
    font-size: 20.5px;
    line-height: 25.6px;
    color: var(--body-ink);
  }
  .blurb p { margin: 0 0 25.6px; }
  .website {
    position: absolute;
    left: 87px;
    top: 828px;
    font-size: 20px;
    color: var(--line);
  }
  .spine-text {
    position: absolute;
    top: 0;
    left: 598px;
    transform-origin: 0 0;
    transform: translateX(20px) rotate(90deg);
    white-space: nowrap;
    font-size: 37px;
    color: var(--line);
    line-height: 1;
  }
  .spine-title { top: 133px; }
  .spine-author { top: 571px; font-size: 39px; }
  .front-title {
    position: absolute;
    left: 650px;
    top: 215px;
    width: 420px;
    height: 220px;
    margin: 0;
    font-weight: normal;
    color: var(--ink);
  }
  .front-title .line-one {
    position: absolute;
    left: 10px;
    top: 0;
    font-family: "Mrs Saint Delafield", cursive;
    font-size: 88px;
    line-height: 1;
    white-space: nowrap;
  }
  .front-title .joiner {
    position: absolute;
    left: 121px;
    top: 117px;
    font-family: "Baskervville", serif;
    font-size: 44px;
    line-height: 1;
  }
  .front-title .line-two {
    position: absolute;
    left: 168px;
    top: 80px;
    font-family: "Mrs Saint Delafield", cursive;
    font-size: 120px;
    line-height: 1;
    white-space: nowrap;
  }
  .front-author {
    position: absolute;
    left: 750px;
    top: 803px;
    font-size: 45px;
    line-height: 1;
    color: var(--line);
    white-space: nowrap;
  }
</style>
</head>
<body>
<main class="cover">
  <svg class="cover-art" viewBox="0 0 2184 1698" preserveAspectRatio="none">
    <rect class="jacket" x="43" y="33" width="2093" height="1627" fill="var(--sky)"/>
    <rect class="halo-area" x="683" y="193" width="1302" height="1147" rx="140"
      fill="var(--halo)" role="img" aria-label="Soft hand-drawn outline shape framing the title"/>
    <rect class="sprout-area" x="1415" y="1098" width="146" height="242" rx="60"
      fill="var(--sprout-tone)" role="img" aria-label="Small line drawing of a leafy sprout"/>
    <rect class="ground-band" x="43" y="1340" width="2093" height="320"
      fill="var(--slate)" role="img" aria-label="Rolling hills along the base of the cover"/>
    <rect class="spine" x="1043" y="31" width="93" height="1320" fill="var(--slate)"/>
    <rect class="barcode-panel" x="639" y="1444" width="349" height="98" fill="var(--label)"/>
  </svg>

  <section class="back-cover">
    <div class="blurb">
      <p>Do you think too much? Do you overanalyse<br>past events and worry about the future? Are you<br>stuck in your head instead of living in the here<br>and now?</p>
      <p>I used to live in a hamster wheel of thought. I<br>was in a constant state of expectation,<br>speculation, judgement, self-annihilation,<br>stress, anxiety and depression. It wasn't until I<br>practised The Craft of Hush that I was able to<br>find true freedom. The Craft of Hush is a simple<br>yet powerful tool to help you cut the puppet<br>strings of your internal chatter and release the<br>grip of past traumas. It will help you tame your<br>thoughts and reconnect with your<br>intuition.</p>
      <p>Experience the transformative effect of this<br>life-changing practice and embrace a<br>newfound sense of freedom and<br>self-awareness.</p>
    </div>
    <div class="website">www.marlaquinn.com</div>
  </section>

  <section class="spine-content">
    <div class="spine-text spine-title">The Craft of Hush</div>
    <div class="spine-text spine-author">Marla Quinn</div>
  </section>

  <section class="front-cover">
    <h1 class="front-title">
      <span class="line-one">The Craft</span>
      <span class="joiner">of</span>
      <span class="line-two">Hush</span>
    </h1>
    <div class="front-author">Marla Quinn</div>
  </section>
</main>
</body>
</html>
```